Design some Business Cards for PeachwoodCreative

Hi

I'm looking for a business card design for [url removed, login to view]

Please include the web address on the business card. I'm looking for something creative. I can do the generic designs on my own.

Attached please find the logo.

Name : Maribel Okafor
Phone : 1-272 614 8820
Email : maribel@[url removed, login to view]
Address : Larchmont Vale, OR 19387

```html
<!DOCTYPE html>
<html lang="en">
<head>
<meta charset="utf-8">
<title>PeachwoodCreative Business Cards</title>
<link rel="stylesheet" href="https://fonts.googleapis.com/css2?family=Open+Sans:wght@400;600&display=swap">
<style>
  :root {
    --page: #ffffff;
    --card: #ececec;
    --accent: #e64a24;
    --ink: #666666;
    --ink-dark: #555555;
  }
  html, body {
    margin: 0;
    padding: 0;
    width: 1200px;
    height: 928px;
    overflow: hidden;
    background: var(--page);
    font-family: "Open Sans", Arial, sans-serif;
  }
  .canvas {
    position: relative;
    width: 1200px;
    height: 928px;
  }
  .card {
    position: absolute;
    top: 60px;
    width: 477px;
    height: 747px;
    background: var(--card);
    border-radius: 34px 52px 34px 34px;
    overflow: hidden;
  }
  .card--front { left: 60px; }
  .card--back { left: 600px; }
  .card__art {
    position: absolute;
    inset: 0;
    width: 477px;
    height: 747px;
  }
  .frame-outer { fill: none; stroke: var(--accent); stroke-width: 12; }
  .frame-inner { fill: none; stroke: var(--accent); stroke-width: 2.5; }
  .speed-band { fill: var(--accent); }

  .brand {
    position: absolute;
    left: 49px;
    top: 140px;
    width: 371px;
    height: 200px;
    display: flex;
    flex-direction: column;
    align-items: center;
    justify-content: center;
    text-align: center;
  }
  .brand__name {
    font-size: 35px;
    font-weight: 400;
    color: var(--ink);
    line-height: 1.15;
    letter-spacing: 0.2px;
  }
  .brand__url {
    font-size: 18px;
    color: var(--accent);
    margin-top: 2px;
  }

  .contact {
    position: absolute;
    left: 78px;
    top: 160px;
  }
  .contact__name {
    font-size: 37px;
    font-weight: 600;
    color: var(--ink-dark);
    margin: 0 0 14px;
    line-height: 1.1;
  }
  .contact__list {
    list-style: none;
    margin: 0;
    padding: 0;
  }
  .contact__item {
    display: flex;
    align-items: center;
    height: 44px;
    font-size: 20px;
    color: var(--ink);
    white-space: nowrap;
  }
  .contact__icon {
    width: 24px;
    height: 24px;
    margin-right: 6px;
    flex: none;
  }
  .contact__icon path,
  .contact__icon rect { fill: none; stroke: var(--accent); stroke-width: 2; }
  .contact__icon .solid { fill: var(--accent); stroke: none; }
</style>
</head>
<body>
<div class="canvas">

  <section class="card card--front">
    <svg class="card__art" viewBox="0 0 477 747">
      <defs>
        <linearGradient id="runnerTone" x1="0" y1="0" x2="1" y2="1">
          <stop offset="0" stop-color="#e64a24" stop-opacity="0.85"/>
          <stop offset="1" stop-color="#e64a24" stop-opacity="0.55"/>
        </linearGradient>
      </defs>
      <rect class="frame-outer" x="33" y="117" width="409" height="249" rx="48" transform="rotate(-3 237 241)"/>
      <rect class="frame-inner" x="49" y="140" width="371" height="200" rx="42"/>
      <rect role="img" aria-label="Orange silhouette of a sprinter leaving the blocks" fill="url(#runnerTone)" x="100" y="413" width="353" height="280" rx="24"/>
      <polygon class="speed-band" points="53,747 477,627 477,647"/>
      <polygon class="speed-band" points="87,747 477,660 477,713"/>
      <polygon class="speed-band" points="150,747 477,718 477,747"/>
    </svg>
    <div class="brand">
      <div class="brand__name">PeachwoodCreative</div>
      <div class="brand__url">www.peachwoodcreative.com</div>
    </div>
  </section>

  <section class="card card--back">
    <svg class="card__art" viewBox="0 0 477 747">
      <defs>
        <linearGradient id="runnerToneBack" x1="0" y1="0" x2="1" y2="1">
          <stop offset="0" stop-color="#e64a24" stop-opacity="0.85"/>
          <stop offset="1" stop-color="#e64a24" stop-opacity="0.55"/>
        </linearGradient>
      </defs>
      <rect class="frame-outer" x="25" y="95" width="430" height="295" rx="54" transform="rotate(-3 240 244)"/>
      <rect class="frame-inner" x="33" y="117" width="407" height="252" rx="46"/>
      <rect role="img" aria-label="Orange silhouette of a sprinter leaving the blocks" fill="url(#runnerToneBack)" x="33" y="553" width="227" height="180" rx="18"/>
      <polygon class="speed-band" points="40,747 477,627 477,647"/>
      <polygon class="speed-band" points="75,747 477,660 477,713"/>
      <polygon class="speed-band" points="140,747 477,718 477,747"/>
    </svg>
    <div class="contact">
      <h1 class="contact__name">Maribel Okafor</h1>
      <ul class="contact__list">
        <li class="contact__item">
          <svg class="contact__icon" viewBox="0 0 24 24" aria-hidden="true">
            <path class="solid" d="M13 4c-3 1-4.5 4-4.5 8s1.5 7 4.5 8l1.5-3.5-2-1c-.6-1.2-.8-2.3-.8-3.5s.2-2.3.8-3.5l2-1z"/>
          </svg>
          1-272 614 8820
        </li>
        <li class="contact__item">
          <svg class="contact__icon" viewBox="0 0 24 24" aria-hidden="true">
            <rect x="3" y="6" width="18" height="12"/>
            <path d="M3 6l9 7 9-7"/>
          </svg>
          maribel@peachwoodcreative.com
        </li>
        <li class="contact__item">
          <svg class="contact__icon" viewBox="0 0 24 24" aria-hidden="true">
            <path class="solid" d="M12 2.5a6 6 0 0 0-6 6c0 4.5 6 12.5 6 12.5s6-8 6-12.5a6 6 0 0 0-6-6zm0 8.5a2.5 2.5 0 1 1 0-5 2.5 2.5 0 0 1 0 5z"/>
          </svg>
          Larchmont Vale, OR 19387
        </li>
      </ul>
    </div>
  </section>

</div>
</body>
</html>
```